Professional DJ Business Card

Business card for giving out to clubs and venues or interested groups that are in need of a professional DJ. I want something artistic and catchy/alluring, with a minimalist approach that gets just the vital amount of info and leaves the rest for inquiry via contacting me. Ideally I would like one side to have an image of something cool like an eye and my name, then the other side be the contact info, I am definitely feeling a black or dark colored card, but I am open to other designs. I am uploading a picture that I made that reflects a little of what I am *kind of* looking for.

Industry/Entity Type

Business

Contact Information for Business Card

Tomas Halvik (Voxtel)
Professional DJ (West Coast)
EDM (Deep/House/Techno), Hip Hop, Latin, Trap.
Cell: 555-274-9163
Email: Voxtelofficial@mailnest.net
www.beatcloudia.net/yourtuneisfading

```html
<!DOCTYPE html>
<html lang="en">
<head>
<meta charset="utf-8">
<title>Tomas Halvik (Voxtel) – DJ Business Card</title>
<link rel="stylesheet" href="https://fonts.googleapis.com/css2?family=Carlito:wght@400;700&family=Pinyon+Script&display=swap">
<style>
  :root {
    --backdrop: #eedcbf;
    --card-black: #0e100e;
    --ink-white: #ffffff;
    --card-shadow: rgba(40, 25, 10, 0.45);
  }
  * { margin: 0; padding: 0; box-sizing: border-box; }
  html, body {
    width: 1189px;
    height: 1200px;
    overflow: hidden;
    background: var(--backdrop);
  }
  .canvas {
    position: relative;
    width: 1189px;
    height: 1200px;
  }
  .card {
    position: absolute;
    left: 183px;
    width: 832px;
    height: 486px;
    background: var(--card-black);
    border-radius: 24px;
    box-shadow: 6px 8px 10px var(--card-shadow);
    color: var(--ink-white);
    text-align: center;
    font-family: "Carlito", "Calibri", sans-serif;
  }
  .card--front { top: 69px; }
  .card--back { top: 628px; }
  .line {
    position: absolute;
    left: 0;
    right: 0;
    white-space: nowrap;
  }
  .brand-mark {
    top: 190px;
    display: flex;
    justify-content: center;
    align-items: center;
    gap: 18px;
    font-size: 84px;
    font-weight: 400;
    line-height: 1;
    letter-spacing: 1px;
  }
  .brand-dot {
    width: 26px;
    height: 26px;
    border-radius: 50%;
    background: var(--ink-white);
  }
  .dj-name {
    font-family: "Pinyon Script", cursive;
    font-size: 58px;
    line-height: 1;
  }
  .card--front .dj-name { top: 334px; }
  .card--front .dj-role { top: 404px; }
  .dj-role { font-size: 26px; line-height: 1; }
  .card--back .dj-name { top: 96px; }
  .card--back .dj-role { top: 164px; }
  .genres { top: 203px; font-size: 22px; line-height: 1; }
  .contact { font-size: 27px; line-height: 1; }
  .contact b { font-weight: 700; }
  .contact--cell { top: 290px; }
  .contact--email { top: 324px; }
  .contact--web { top: 373px; font-size: 26px; }
</style>
</head>
<body>
  <main class="canvas">
    <section class="card card--front">
      <div class="line brand-mark"><span class="brand-dot"></span><span>Voxtel</span></div>
      <h1 class="line dj-name">Tomas Halvik (Voxtel)</h1>
      <p class="line dj-role">Professional DJ (West Coast)</p>
    </section>

    <section class="card card--back">
      <h2 class="line dj-name">Tomas Halvik (Voxtel)</h2>
      <p class="line dj-role">Professional DJ (West Coast)</p>
      <p class="line genres">EDM (Deep/House/Techno), Hip Hop, Latin, Trap.</p>
      <p class="line contact contact--cell"><b>Cell:</b> 555-274-9163</p>
      <p class="line contact contact--email"><b>Email:</b> Voxtelofficial@mailnest.net</p>
      <p class="line contact contact--web">www.beatcloudia.net/yourtuneisfading</p>
    </section>
  </main>
</body>
</html>
```